Medical Device Packaging Project 3 of 5

We are a medical device startup company needing packaging for a total of 5 device brands. This is posting 3 of 5 and the device name is "Vosmi"

Vosmi is an intraocular lens for use in cataract surgery. The target market is Chinese ophthalmologists. The box should be sophisticated and upmarket.

The company name is Kemberly Optics, I have included the logo in the uploaded files section. You should include the logo on the box.

I have uploaded a sample lens boxes from other companies that demonstrate the information needed to be contained on the box in terms of address, warnings, symbols, etc.

I have also uploaded the blank dieline of the boxes

You are welcome and encouraged to also submit to projects 1, 2, 4, and 5 as well. The same rules and expectations apply.

Requirements
Should not have
• Should not have any images of an eye or any bionic/futuristic feel to the design
• Note that the tavilens box is for text reference only. You may use the lens image but the futuristic/bionic look is NOT what we are going for with this brand. It should be traditional upmarket medical device artwork.

```html
<!DOCTYPE html>
<html lang="en">
<head>
<meta charset="utf-8">
<title>Vosmi – Intraocular Lens Carton Dieline</title>
<link href="https://fonts.googleapis.com/css2?family=Montserrat:wght@400;500;600&family=Roboto+Condensed:wght@400&family=Noto+Sans+SC:wght@400&family=Tinos&display=swap" rel="stylesheet">
<style>
  :root{
    --teal:#1ad5d6;
    --teal-deep:#0fbcbf;
    --ink:#1f8d90;
    --ink-dark:#2a4f55;
    --flap:#b3f4f4;
    --panel-light:#effdfd;
    --panel-cyan:#c6f6f6;
    --tile:#8ff0f0;
    --tile-dark:#12c8cb;
    --dim:#555;
  }
  *{margin:0;padding:0;box-sizing:border-box}
  html,body{width:800px;height:1200px;overflow:hidden;background:#fff}
  .canvas{position:relative;width:800px;height:1200px;overflow:hidden;font-family:"Montserrat",sans-serif}
  .dieline{position:absolute;left:0;top:0}
  .abs{position:absolute}

  .dim{position:absolute;font-family:"Tinos",serif;font-size:11px;color:var(--dim);white-space:nowrap}
  .dim.vertical{transform:rotate(-90deg);transform-origin:center}

  .tile-field{position:absolute;border-radius:4px;
    background:linear-gradient(135deg,var(--tile-dark) 0%,var(--tile) 60%,rgba(143,240,240,.35) 100%)}
  .tile-field.soft{background:linear-gradient(135deg,var(--tile) 0%,rgba(143,240,240,.3) 100%)}

  .front{position:absolute;left:199.6px;top:192px;width:409.6px;height:378px;overflow:hidden;
    background:linear-gradient(180deg,#fff 0%,var(--panel-light) 100%)}
  .front .right-half{position:absolute;inset:0;clip-path:polygon(52% 0,100% 0,100% 100%,47% 100%);
    background:linear-gradient(180deg,#e6fcfc 0%,var(--panel-cyan) 100%)}
  .back{position:absolute;left:199.6px;top:717px;width:409.6px;height:378px;overflow:hidden;
    background:linear-gradient(90deg,#fff 0%,var(--panel-light) 45%,#dcfafa 100%)}

  .lens{position:absolute;border-radius:50%;
    background:radial-gradient(circle at 60% 40%,#fff 0%,#c8f7f7 45%,#7fe6e6 100%);
    box-shadow:0 0 0 2px rgba(255,255,255,.8),0 6px 14px rgba(31,141,144,.25)}
  .lens-haptics{position:absolute;border-radius:50%;
    background:radial-gradient(ellipse at center,rgba(150,225,225,.45) 0%,rgba(150,225,225,0) 70%)}

  .brand{position:absolute;text-align:center;color:var(--ink);font-weight:500;line-height:1}
  .brand .name{display:block;letter-spacing:1px}
  .brand .sub{display:block;letter-spacing:6px;margin-top:4px}

  .product{position:absolute;color:var(--ink);font-weight:600;line-height:1;letter-spacing:1px}
  .tagline{position:absolute;color:var(--ink);font-weight:400;line-height:1.15;text-transform:uppercase}

  .company-address{position:absolute;transform:rotate(180deg);text-align:right;
    font-size:10px;line-height:1.35;color:var(--ink-dark);letter-spacing:.5px}

  .info-column{position:absolute;left:431px;top:727px;width:175px}
  .info-block{border-left:2px solid var(--ink-dark);padding-left:5px;margin-bottom:9px;
    font-family:"Roboto Condensed",sans-serif;font-size:7.4px;line-height:1.35;color:var(--ink-dark);text-transform:uppercase}
  .info-block.zh{font-family:"Noto Sans SC",sans-serif;font-size:8px;letter-spacing:2px;line-height:1.3}
  .divider{position:absolute;left:405px;top:717px;width:2px;height:378px;background:var(--teal)}

  .symbols{position:absolute;display:flex;align-items:center;gap:8px}
  .sterile{display:flex;border:1px solid var(--ink-dark);font-family:"Roboto Condensed",sans-serif;font-size:7px;color:var(--ink-dark)}
  .sterile span{padding:3px 3px}
  .sterile span+span{border-left:1px solid var(--ink-dark)}
  .symbols.vertical{flex-direction:column}
</style>
</head>
<body>
<div class="canvas">

  <!-- Panel shapes -->
  <svg class="dieline" width="800" height="1200" viewBox="0 0 800 1200">
    <!-- top dust flaps -->
    <polygon points="87.6,62 184,45 199.6,45 199.6,180 186,192 87.6,192" fill="var(--flap)"/>
    <polygon points="721.2,62 624.8,45 609.2,45 609.2,180 622.8,192 721.2,192" fill="var(--flap)"/>
    <!-- top panel -->
    <rect x="199.6" y="45" width="409.6" height="147" fill="var(--teal)"/>
    <!-- glue / side flaps -->
    <rect x="30" y="196" width="70" height="370" rx="12" fill="var(--flap)"/>
    <rect x="708.8" y="196" width="70" height="370" rx="12" fill="var(--flap)"/>
    <!-- side panels -->
    <rect x="87.6" y="192" width="112" height="378" fill="var(--teal)"/>
    <rect x="609.2" y="192" width="112" height="378" fill="var(--teal)"/>
    <!-- bottom dust flaps -->
    <polygon points="87.6,580 186,570 199.6,570 199.6,717 186,717 87.6,705" fill="var(--flap)"/>
    <polygon points="721.2,580 622.8,570 609.2,570 609.2,717 622.8,717 721.2,705" fill="var(--flap)"/>
    <!-- bottom band -->
    <rect x="199.6" y="570" width="409.6" height="147" fill="var(--teal)"/>
    <!-- tuck flap -->
    <rect x="199.6" y="1095" width="409.6" height="50" fill="var(--flap)"/>
  </svg>

  <!-- Dimensions -->
  <div class="dim" style="left:128px;top:24px">35mm</div>
  <div class="dim" style="left:386px;top:24px">128mm</div>
  <div class="dim" style="left:650px;top:24px">35mm</div>
  <div class="dim" style="left:38px;top:176px">18mm</div>
  <div class="dim" style="left:740px;top:176px">18mm</div>
  <div class="dim vertical" style="left:56px;top:110px">35mm</div>
  <div class="dim vertical" style="left:-4px;top:374px">90mm</div>
  <div class="dim vertical" style="left:56px;top:636px">35mm</div>
  <div class="dim vertical" style="left:168px;top:898px">90mm</div>
  <div class="dim vertical" style="left:168px;top:1112px">12mm</div>

  <!-- Top panel -->
  <div class="tile-field soft" style="left:222px;top:52px;width:65px;height:132px" role="img" aria-label="Decorative square tile mosaic"></div>
  <div class="tile-field soft" style="left:312px;top:100px;width:66px;height:84px" role="img" aria-label="Decorative square tile mosaic"></div>
  <div class="company-address" style="left:428px;top:108px;width:156px">
    KEMBERLY OPTICS LIMITED<br>HONG KONG<br>www.kemberlyoptics.com
  </div>

  <!-- Left side panel -->
  <div class="tile-field soft" style="left:121px;top:198px;width:63px;height:90px" role="img" aria-label="Decorative square tile mosaic"></div>

  <!-- Front panel -->
  <section class="front">
    <div class="right-half"></div>
    <div class="tile-field" style="left:4px;top:5px;width:175px;height:134px" role="img" aria-label="Decorative square tile mosaic"></div>
    <div class="tile-field" style="left:229px;top:239px;width:177px;height:137px" role="img" aria-label="Decorative square tile mosaic"></div>
    <div class="lens-haptics" style="left:130px;top:50px;width:130px;height:300px" role="img" aria-label="Intraocular lens with curved haptics"></div>
    <div class="lens" style="left:141px;top:134px;width:110px;height:120px"></div>
    <div class="brand" style="left:250px;top:70px;width:170px">
      <span class="name" style="font-size:22px">KEMBERLY</span>
      <span class="sub" style="font-size:8px">OPTICS</span>
    </div>
    <div class="tagline" style="left:250px;top:160px;width:170px;text-align:center;font-size:10px">Hydrophobic acrylic<br>intraocular lens</div>
    <div class="product" style="left:5px;top:319px;font-size:30px">VOSMI</div>
    <div class="tagline" style="left:5px;top:355px;font-size:10px">With 360° square edge</div>
  </section>

  <!-- Right side panel -->
  <div class="brand" style="left:632px;top:240px;width:80px;transform:rotate(-90deg);color:var(--ink-dark)">
    <span class="name" style="font-size:10px">KEMBERLY</span>
    <span class="sub" style="font-size:5px;letter-spacing:3px">OPTICS</span>
  </div>
  <div class="symbols vertical" style="left:688px;top:390px">
    <svg width="14" height="14" viewBox="0 0 14 14"><circle cx="7" cy="7" r="6" fill="none" stroke="var(--ink-dark)"/><line x1="3" y1="3" x2="11" y2="11" stroke="var(--ink-dark)"/></svg>
    <svg width="14" height="14" viewBox="0 0 14 14"><circle cx="7" cy="7" r="6" fill="none" stroke="var(--ink-dark)"/><line x1="3" y1="11" x2="11" y2="3" stroke="var(--ink-dark)"/></svg>
    <svg width="14" height="14" viewBox="0 0 14 14"><circle cx="7" cy="7" r="6" fill="none" stroke="var(--ink-dark)"/><text x="7" y="10" font-size="8" text-anchor="middle" fill="var(--ink-dark)" font-family="Montserrat,sans-serif">2</text></svg>
    <svg width="14" height="14" viewBox="0 0 14 14"><polygon points="7,1 13,13 1,13" fill="none" stroke="var(--ink-dark)"/></svg>
  </div>
  <div class="sterile abs" style="left:686px;top:520px;transform:rotate(-90deg);font-size:5px"><span>STERILE</span><span>EO</span></div>
  <div class="tile-field soft" style="left:630px;top:471px;width:55px;height:92px" role="img" aria-label="Decorative square tile mosaic"></div>

  <!-- Bottom band -->
  <div class="brand" style="left:212px;top:630px;width:92px">
    <span class="name" style="font-size:15px">KEMBERLY</span>
    <span class="sub" style="font-size:6px;letter-spacing:4px">OPTICS</span>
  </div>
  <div class="product" style="left:311px;top:612px;font-size:20px">VOSMI</div>
  <div class="tagline" style="left:311px;top:636px;font-size:7.5px;color:var(--panel-light)">Hydrophobic acrylic<br>intraocular lens<br>with 360° square edge</div>
  <div class="tile-field soft" style="left:436px;top:572px;width:64px;height:92px" role="img" aria-label="Decorative square tile mosaic"></div>
  <div class="tile-field soft" style="left:522px;top:572px;width:70px;height:142px" role="img" aria-label="Decorative square tile mosaic"></div>

  <!-- Back panel -->
  <section class="back">
    <div class="tile-field" style="left:4px;top:5px;width:146px;height:136px" role="img" aria-label="Decorative square tile mosaic"></div>
    <div class="tile-field" style="left:4px;top:237px;width:146px;height:136px" role="img" aria-label="Decorative square tile mosaic"></div>
    <div class="lens-haptics" style="left:120px;top:85px;width:100px;height:210px" role="img" aria-label="Intraocular lens with curved haptics"></div>
    <div class="lens" style="left:137px;top:150px;width:66px;height:72px"></div>
  </section>
  <div class="divider"></div>
  <div class="info-column">
    <div class="info-block">Contains one sterile intraocular lens<br>Do not use if the package is damaged<br>Do not resterilize</div>
    <div class="info-block zh">内含无菌的眼内透镜一个<br>如果包装被损坏，请勿使用<br>请勿重新消毒</div>
    <div class="info-block">Contient une stérile lentille intraoculaire<br>Ne pas utiliser si le forfait est endommagé<br>Ne pas restériliser</div>
    <div class="info-block">Contiene uno sterile lente intraoculare<br>Non usare se il pacchetto è danneggiato<br>Non risterilizzare</div>
    <div class="info-block">Enthält eine sterilische intraokulare Linse<br>Nicht verwenden, wenn das Paket schädigt wird<br>Nicht resterilieren</div>
    <div class="info-block">Bevat één steriele intraoculaire lens<br>Niet gebruiken als de verpakking beschadigd is<br>Niet opnieuw steriliseren</div>
  </div>
  <div class="symbols" style="left:431px;top:1052px">
    <div class="sterile"><span>STERILE</span><span>EO</span></div>
    <svg width="20" height="20" viewBox="0 0 20 20"><polygon points="10,2 18,18 2,18" fill="none" stroke="var(--ink-dark)"/><line x1="10" y1="8" x2="10" y2="13" stroke="var(--ink-dark)"/><circle cx="10" cy="15.5" r=".8" fill="var(--ink-dark)"/></svg>
    <svg width="20" height="20" viewBox="0 0 20 20"><circle cx="10" cy="10" r="8" fill="none" stroke="var(--ink-dark)"/><text x="10" y="14" font-size="11" text-anchor="middle" fill="var(--ink-dark)" font-family="Montserrat,sans-serif">2</text><line x1="4" y1="16" x2="16" y2="4" stroke="var(--ink-dark)"/></svg>
    <svg width="20" height="20" viewBox="0 0 20 20"><circle cx="10" cy="10" r="8" fill="none" stroke="var(--ink-dark)"/><line x1="4" y1="4" x2="16" y2="16" stroke="var(--ink-dark)"/></svg>
    <svg width="20" height="20" viewBox="0 0 20 20"><circle cx="10" cy="10" r="8" fill="none" stroke="var(--ink-dark)"/><rect x="6" y="6" width="8" height="8" fill="none" stroke="var(--ink-dark)"/><line x1="4" y1="16" x2="16" y2="4" stroke="var(--ink-dark)"/></svg>
  </div>

</div>
</body>
</html>
```